Brenwick Structures Construction Company Seeking Modern Website

We are a small construction company wanting to create a web presence. We don't have much in the way of current content but will get photos as they come in. Attached is a picture of our business card.
The pages we would like on the menu are:
Home
Portfolio
Product Specs
Testimonials
Our Process
Contact
Some designs we like are:
http://www.tovandrafters.example/
http://www.qrkframes.example/
http://harnestshed.example/
http://pellowbarns.example/
Not much requirements other than that so feel free to be creative!
Target Market(s)
Construction
Commercial and Residential Buildings
Industry/Entity Type
Construction Company
Number of Pages Required
5+ page

```html
<!DOCTYPE html>
<html lang="en">
<head>
<meta charset="utf-8">
<title>Brenwick Structures</title>
<link href="https://fonts.googleapis.com/css2?family=Roboto:ital,wght@0,400;0,500;0,700;0,900;1,400;1,900&family=Courgette&display=swap" rel="stylesheet">
<style>
:root{
  --blue:#0b9fdc;
  --blue-dark:#0a7fb4;
  --red:#d93025;
  --dark:#1c1c1c;
  --text:#555;
  --line:#d2d2d2;
  --white:#fff;
}
*{margin:0;padding:0;box-sizing:border-box}
html,body{width:1200px;height:2449px;overflow:hidden;background:#fff}
body{position:relative;font-family:"Roboto",sans-serif;color:var(--text)}
.abs{position:absolute}

/* header */
.site-header{left:0;top:0;width:1200px;height:163px;background:linear-gradient(#2b2b2b,#111)}
.brand{left:39px;top:55px;display:flex;align-items:center;gap:12px;font-weight:900;font-size:38px;color:var(--blue);letter-spacing:-1px}
.brand-mark{width:24px;height:24px;background:var(--red);border-radius:50%}
.call{left:660px;top:40px;display:flex;gap:14px;align-items:center;color:#fff}
.call-label{font-size:17px;font-weight:500;line-height:1}
.call-number{font-size:33px;color:var(--blue);line-height:1.1}
.header-divider{left:963px;top:38px;width:1px;height:46px;background:#555}
.social-top{left:969px;top:42px;display:flex;gap:9px}
.social-top span{width:33px;height:33px;border:2px solid #777;border-radius:50%}
.main-nav{left:408px;top:114px;width:792px;height:49px;background:linear-gradient(#20b2ee,var(--blue-dark));clip-path:polygon(26px 0,100% 0,100% 100%,0 100%);display:flex;align-items:center;padding-left:27px}
.main-nav a{color:#fff;text-decoration:none;font-size:17.5px;font-weight:500;margin-right:24px}

/* hero */
.hero{left:0;top:163px;width:1200px;height:531px;background:linear-gradient(180deg,#7fa36a 0%,#a7703f 35%,#b8855a 60%,#8c7f6b 85%,#6f8a4f 100%)}
.hero-title{left:88px;top:190px;font-family:"Courgette",cursive;font-size:46px;line-height:56px;color:#fff;text-shadow:2px 2px 0 #222}
.hero-arrow{top:385px;width:18px;height:74px;background:rgba(40,40,40,.8)}
.hero-arrow.prev{left:0}
.hero-arrow.next{left:1182px;background:var(--blue)}
.hero-dots{left:552px;top:656px;display:flex;gap:7px}
.hero-dots span{width:14px;height:14px;border-radius:50%;background:rgba(255,255,255,.85)}
.hero-dots span.on{background:var(--blue);border:2px solid #fff}

/* welcome */
.welcome-kicker{left:104px;top:730px;font-size:21px;color:#333}
.welcome-title{left:75px;top:748px;font-size:54px;font-weight:900;font-style:italic;color:var(--blue);letter-spacing:-1px}
.welcome-rule{left:72px;top:825px;width:694px;height:6px;background:var(--line)}
.welcome-copy{left:72px;top:852px;width:694px;font-size:13.6px;line-height:21.8px;color:#666}

/* contact form */
.contact-card{left:794px;top:669px;width:333px;height:428px;background:var(--blue);box-shadow:0 12px 14px -10px rgba(0,0,0,.3)}
.contact-head{left:0;top:0;width:333px;height:82px;background:var(--red);padding:14px 0 0 14px;color:#fff}
.contact-head h3{font-size:31px;font-weight:900;font-style:italic;line-height:1}
.contact-head p{font-size:15.5px;font-weight:700;margin-top:4px}
.field{left:14px;width:304px;height:39px;background:#fff;font-size:13px;color:#777;padding:11px 10px}
.submit{left:14px;top:371px;width:95px;height:43px;background:var(--red);color:#fff;font-size:16px;font-weight:700;text-align:center;line-height:43px}

/* tabs */
.tab{top:1158px;height:50px;display:flex;align-items:center;gap:8px;padding-left:14px;color:#fff;font-size:30px;font-weight:900;font-style:italic;letter-spacing:-.5px}
.tab.residential{left:73px;width:242px;background:var(--blue)}
.tab.commercial{left:315px;width:245px;background:#b8b8b8}
.tab-rule{left:0;top:1208px;width:1200px;height:6px;background:var(--blue)}
.feature{left:0;top:1214px;width:1200px;height:497px;background:linear-gradient(90deg,#e4e4e4 0%,#e2e2e2 32%,#bdbdbd 55%,#8f8f8f 75%,#9a9a9a 100%)}
.feature-copy{left:78px;top:1380px;width:455px;font-size:13.6px;line-height:21.8px;color:#555}
.btn-more{display:flex;align-items:center;color:#fff;background:var(--blue-dark);font-size:17px;clip-path:polygon(10px 0,100% 0,calc(100% - 10px) 100%,0 100%)}
.btn-more .label{flex:1;padding-left:18px}
.btn-more .chev{width:46px;height:100%;background:#105a80;display:flex;align-items:center;justify-content:center}
.feature .btn-more{position:absolute;left:111px;top:452px;width:170px;height:45px}

/* testimonial and news */
.block-title{top:1776px;font-size:33px;font-weight:900;font-style:italic;color:#111;letter-spacing:-1px}
.block-rule{top:1822px;height:5px;background:var(--blue-dark)}
.block-nav{top:1786px;display:flex;gap:14px}
.quote-box{left:73px;top:1850px;width:49px;height:49px;background:#c9c9c9;color:#fff;font-size:56px;font-weight:900;line-height:60px;text-align:center;font-style:italic}
.quote-copy{left:137px;top:1864px;width:450px;font-size:14.3px;line-height:21.4px;font-style:italic;color:#666}
.avatar{left:134px;top:1983px;width:52px;height:52px;border-radius:50%;background:linear-gradient(#d6b28f,#8a6a4d);border:3px solid var(--blue)}
.person{left:196px;top:1988px;font-size:14.5px;color:#222;font-weight:500}
.person small{display:block;font-size:12px;color:#777;font-weight:400;margin-top:2px}
.news-date{left:614px;top:1864px;font-size:12px;color:#888}
.news-title{left:614px;top:1885px;font-size:16.5px;color:var(--blue-dark);font-weight:500}
.news-copy{left:614px;top:1912px;width:513px;font-size:14.3px;line-height:21.4px;color:#666}
.news .btn-more{position:absolute;left:614px;top:2037px;width:142px;height:38px;font-size:14px}

/* footer */
.site-footer{left:0;top:2118px;width:1200px;height:296px;background:repeating-linear-gradient(45deg,#262626 0 2px,#222 2px 4px)}
.foot-col{top:2150px;width:248px}
.foot-col h4{color:#fff;font-size:18.5px;font-weight:500;padding-bottom:10px;border-bottom:1px solid #444;margin-bottom:12px}
.foot-links a{display:block;color:#cfcfcf;font-size:13.5px;text-decoration:none;line-height:26px}
.foot-contact li{list-style:none;display:flex;gap:12px;color:#cfcfcf;font-size:13.5px;line-height:19px;margin-bottom:18px}
.foot-contact svg{flex:none;margin-top:3px}
.map{width:245px;height:155px;background:linear-gradient(135deg,#e8e3d2,#cfd9c0 50%,#d9e4ee)}
.foot-social li{list-style:none;display:flex;align-items:center;gap:10px;color:#e6e6e6;font-size:14.5px;margin-bottom:11px}
.foot-social span{width:35px;height:35px;border:2px solid #ddd;border-radius:50%}
.bottom-bar{left:0;top:2414px;width:1200px;height:35px;background:#141414;color:#aaa;font-size:12.5px;line-height:35px;padding-left:77px}
</style>
</head>
<body>

<header class="abs site-header">
  <div class="abs brand"><span class="brand-mark"></span>Brenwick Structures</div>
  <div class="abs call">
    <svg width="40" height="40" viewBox="0 0 24 24" fill="#fff"><path d="M6.6 10.8a15.1 15.1 0 0 0 6.6 6.6l2.2-2.2c.3-.3.7-.4 1-.2 1.1.4 2.300.6 3.6.6.6 0 1 .4 1 1V20c0 .6-.4 1-1 1A17 17 0 0 1 3 4c0-.6.4-1 1-1h3.5c.6 0 1 .4 1 1 0 1.3.2 2.5.6 3.6.1.3 0 .7-.2 1z"/></svg>
    <div><div class="call-label">CALL US TODAY!</div><div class="call-number">1.800.555.0142</div></div>
  </div>
  <div class="abs header-divider"></div>
  <div class="abs social-top"><span></span><span></span><span></span><span></span></div>
  <nav class="abs main-nav">
    <a>HOME</a><a>PORTFOLIO</a><a>PRODUCT SPECS</a><a>TESTIMONIALS</a><a>OUR PROCESS</a><a>CONTACT</a>
  </nav>
</header>

<section class="abs hero" role="img" aria-label="Photo of a wood-sided house with a stone facade and steep gabled roofs"></section>
<h1 class="abs hero-title">Building Dreams,<br>So you Can Build Memories</h1>
<div class="abs hero-arrow prev"></div>
<div class="abs hero-arrow next"></div>
<div class="abs hero-dots"><span class="on"></span><span></span><span></span><span></span><span></span></div>

<div class="abs welcome-kicker">WELCOME TO</div>
<h2 class="abs welcome-title">Brenwick Structures</h2>
<div class="abs welcome-rule"></div>
<p class="abs welcome-copy">Lorem ipsum dolor sit amet, consectetur adipiscing elit, sed do eiusmod tempor incididunt ut labore et dolore magna aliqua. Ut enim ad minim veniam, quis nostrud exercitation ullamco laboris nisi ut aliquip ex ea commodo consequat. Duis aute irure dolor in reprehenderit in voluptate velit esse cillum dolore eu fugiat nulla pariatur. Excepteur sint occaecat cupidatat non proident, sunt in culpa qui officia deserunt mollit anim id est laborum. Lorem ipsum dolor sit amet, consectetur adipiscing elit, sed do eiusmod tempor incididunt ut labore et dolore magna aliqua. Ut enim ad minim veniam, quis nostrud exercitation ullamco laboris nisi ut aliquip ex ea commodo consequat. Duis aute irure dolor in reprehenderit in voluptate velit esse cillum dolore eu fugiat nulla pariatur. Excepteur sint occaecat cupidatat non proident, sunt in culpa qui officia deserunt mollit anim id est laborum.</p>

<form class="abs contact-card">
  <div class="abs contact-head"><h3>Contact Us</h3><p>FOR A FREE CONSULTATION TODAY!</p></div>
  <div class="abs field" style="top:100px">Name</div>
  <div class="abs field" style="top:149px">Email</div>
  <div class="abs field" style="top:198px">Phone</div>
  <div class="abs field" style="top:247px;height:114px">Message</div>
  <div class="abs submit">SUBMIT</div>
</form>

<div class="abs tab residential">
  <svg width="24" height="24" viewBox="0 0 24 24" fill="#fff"><path d="M12 2 1 12h3v10h6v-6h4v6h6V12h3z"/></svg>Residental
</div>
<div class="abs tab commercial">
  <svg width="22" height="24" viewBox="0 0 22 24" fill="#fff"><path d="M2 1h18v23h-7v-5H9v5H2zM5 4v3h3V4zm5 0v3h3V4zm5 0v3h2V4zM5 9v3h3V9zm5 0v3h3V9zm5 0v3h2V9zM5 14v3h3v-3zm5 0v3h3v-3zm5 0v3h2v-3z"/></svg>Commercial
</div>
<div class="abs tab-rule"></div>
<section class="abs feature" role="img" aria-label="Greyscale photo of a row of suburban houses with porches">
  <a class="btn-more"><span class="label">Learn more</span><span class="chev"><svg width="12" height="18" viewBox="0 0 12 18"><path d="M2 2l7 7-7 7" stroke="#fff" stroke-width="3" fill="none"/></svg></span></a>
</section>
<p class="abs feature-copy">Sed ut perspiciatis unde omnis iste natus error sit voluptatem accusantium doloremque laudantium, totam rem aperiam, eaque ipsa quae ab illo inventore veritatis et quasi architecto beatae vitae dicta sunt explicabo. Nemo enim ipsam voluptatem quia voluptas sit aspernatur aut odit aut fugit, sed quia consequuntur magni dolores eos qui ratione voluptatem sequi nesciunt.</p>

<section class="testimonial">
  <h3 class="abs block-title" style="left:72px">Testimonial</h3>
  <div class="abs block-nav" style="left:543px">
    <svg width="12" height="18" viewBox="0 0 12 18"><path d="M10 2 3 9l7 7" stroke="#888" stroke-width="3" fill="none"/></svg>
    <svg width="12" height="18" viewBox="0 0 12 18"><path d="M2 2l7 7-7 7" stroke="#0a7fb4" stroke-width="3" fill="none"/></svg>
  </div>
  <div class="abs block-rule" style="left:72px;width:513px"></div>
  <div class="abs quote-box">“</div>
  <p class="abs quote-copy">Sed ut perspiciatis unde omnis iste natus error sit voluptatem accusantium doloremque laudantium, totam rem aperiam, eaque ipsa quae ab illo inventore veritatis et quasi architecto beatae vitae dicta sunt explicabo. Nemo enim ipsam voluptatem quia voluptas sit aspernatur aut odit aut fugit.</p>
  <div class="abs avatar" role="img" aria-label="Customer portrait"></div>
  <div class="abs person">Dana Whitfield<small>Happy Customer</small></div>
</section>

<section class="news">
  <h3 class="abs block-title" style="left:614px">Latest News</h3>
  <div class="abs block-nav" style="left:1085px">
    <svg width="12" height="18" viewBox="0 0 12 18"><path d="M10 2 3 9l7 7" stroke="#888" stroke-width="3" fill="none"/></svg>
    <svg width="12" height="18" viewBox="0 0 12 18"><path d="M2 2l7 7-7 7" stroke="#0a7fb4" stroke-width="3" fill="none"/></svg>
  </div>
  <div class="abs block-rule" style="left:614px;width:513px"></div>
  <div class="abs news-date">10 Nov 2015</div>
  <div class="abs news-title">Sed ut perspiciatis unde omnis iste natus error sit.</div>
  <p class="abs news-copy">Voluptatem accusantium doloremque laudantium, totam rem aperiam, eaque ipsa quae ab illo inventore veritatis et quasi architecto beatae vitae dicta sunt explicabo. totam rem aperiam, eaque ipsa quae ab illo inventore veritatis et quasi architecto beatae vitae dicta sunt explicabo. totam rem aperiam, eaque ipsa quae.</p>
  <a class="btn-more"><span class="label">Learn more</span><span class="chev" style="width:40px"><svg width="11" height="16" viewBox="0 0 12 18"><path d="M2 2l7 7-7 7" stroke="#fff" stroke-width="3" fill="none"/></svg></span></a>
</section>

<footer class="abs site-footer"></footer>
<div class="abs foot-col foot-links" style="left:72px">
  <h4>Quick Links</h4>
  <a>Home</a><a>Portfolio</a><a>Product Specs</a><a>Testimonials</a><a>Our Process</a><a>Contact</a>
</div>
<div class="abs foot-col" style="left:343px">
  <h4>Contact Address</h4>
  <ul class="foot-contact">
    <li><svg width="12" height="16" viewBox="0 0 12 16" fill="#ddd"><path d="M6 0a6 6 0 0 0-6 6c0 4.5 6 10 6 10s6-5.5 6-10a6 6 0 0 0-6-6zm0 8.5A2.5 2.5 0 1 1 6 3.5a2.5 2.5 0 0 1 0 5z"/></svg><span>228, Lorem Ipsum dolor sit,<br>Dosis amet sit - 85485</span></li>
    <li><svg width="14" height="14" viewBox="0 0 24 24" fill="#ddd"><path d="M6.6 10.8a15.1 15.1 0 0 0 6.6 6.6l2.2-2.2c.3-.3.7-.4 1-.2 1.1.4 2.3.6 3.6.6.6 0 1 .4 1 1V20c0 .6-.4 1-1 1A17 17 0 0 1 3 4c0-.6.4-1 1-1h3.5c.6 0 1 .4 1 1 0 1.3.2 2.5.6 3.6.1.3 0 .7-.2 1z"/></svg><span>Call Us<br>1.800.555.0142</span></li>
    <li><svg width="14" height="11" viewBox="0 0 14 11" fill="#ddd"><path d="M0 0h14v11H0zm1 1.5v.4l6 4 6-4v-.4z"/></svg><span>Email Us<br>info@brenwickstructures.example</span></li>
  </ul>
</div>
<div class="abs foot-col" style="left:612px">
  <h4>Location Map</h4>
  <div class="map" role="img" aria-label="Street map showing the office location"></div>
</div>
<div class="abs foot-col" style="left:883px">
  <h4>Keep In Touch</h4>
  <ul class="foot-social">
    <li><span></span>Tessaloo</li>
    <li><span></span>Wirvane</li>
    <li><span></span>Plombrix</li>
    <li><span></span>Quendlor</li>
  </ul>
</div>
<div class="abs bottom-bar">Copyright © 2015 Brenwick Structures. | Terms of Use &nbsp;| &nbsp;Privacy Policy &nbsp;| &nbsp;Sitemap</div>

</body>
</html>
```